Business Consulting Business Card

professional business card with basic information (1) First and Last name (2) email address, (3) phone number, (4) website.

```html
<!DOCTYPE html>
<html lang="en">
<head>
<meta charset="utf-8">
<title>Tide Harbor Business Card</title>
<link href="https://fonts.googleapis.com/css2?family=Poppins:wght@300;400;500&display=swap" rel="stylesheet">
<style>
  :root {
    --bg: #2b2d30;
    --navy: #0b2a40;
    --navy-deep: #062033;
    --teal: #3fb8b4;
    --sky: #4aa0c4;
    --ink: #3a3f45;
    --ink-dark: #1d3346;
    --white: #ffffff;
  }
  * { margin: 0; padding: 0; box-sizing: border-box; }
  html, body { width: 1200px; height: 960px; overflow: hidden; }
  body {
    background: var(--bg);
    font-family: "Poppins", sans-serif;
    position: relative;
  }
  .card {
    position: absolute;
    left: 290px;
    width: 620px;
    height: 354px;
    border-radius: 22px;
    overflow: hidden;
  }
  .card-back { top: 76px; background: var(--navy); }
  .card-front { top: 506px; background: var(--white); }

  .back-pattern {
    position: absolute; inset: 0;
    background: radial-gradient(ellipse at 30% 70%, #124668 0%, var(--navy) 60%, var(--navy-deep) 100%);
  }
  .back-brand {
    position: absolute; right: 30px; bottom: 30px;
    display: flex; align-items: center; gap: 8px;
    color: var(--white); font-size: 15px; font-weight: 500; letter-spacing: 2px;
  }
  .brand-dot { width: 14px; height: 14px; border-radius: 50%; background: currentColor; }

  .wave { position: absolute; inset: 0; }
  .person {
    position: absolute; right: 40px; top: 26px; text-align: right; color: var(--white);
  }
  .person-name { font-size: 22px; font-weight: 500; line-height: 1.1; }
  .person-title { font-size: 12px; font-weight: 300; }

  .brand {
    position: absolute; left: 44px; top: 224px;
    display: flex; align-items: center; gap: 12px;
    color: var(--ink-dark); font-size: 26px; font-weight: 400; letter-spacing: 6px;
  }
  .brand .brand-dot { width: 34px; height: 34px; background: var(--teal); }

  .contacts {
    position: absolute; left: 48px; bottom: 22px;
    list-style: none; color: var(--ink); font-size: 13px; line-height: 1.45;
  }
  .contacts li { display: flex; align-items: center; gap: 8px; }
  .contacts svg { width: 11px; height: 11px; fill: var(--sky); flex: none; }

  .address {
    position: absolute; right: 36px; bottom: 72px;
    text-align: right; color: var(--ink); font-size: 13px; line-height: 1.4;
  }
</style>
</head>
<body>

<section class="card card-back">
  <div class="back-pattern" role="img" aria-label="Repeating pattern of the company mark in muted blue tones"></div>
  <div class="back-brand"><span class="brand-dot"></span>TIDE HARBOR</div>
</section>

<section class="card card-front">
  <svg class="wave" viewBox="0 0 620 354" preserveAspectRatio="none">
    <defs>
      <linearGradient id="waveFill" x1="0" y1="1" x2="1" y2="0">
        <stop offset="0" stop-color="var(--sky)"/>
        <stop offset="0.5" stop-color="var(--teal)"/>
        <stop offset="1" stop-color="var(--sky)"/>
      </linearGradient>
    </defs>
    <path d="M0,0 H620 V40 C585,95 505,118 400,128 C260,141 140,128 90,158 C50,182 20,205 0,228 Z" fill="url(#waveFill)"/>
    <path d="M624,40 C588,99 505,122 400,132 C260,145 142,132 93,162 C53,186 22,210 -4,238" fill="none" stroke="var(--white)" stroke-width="3"/>
    <path d="M624,45 C588,105 505,128 400,138 C260,151 145,138 96,168 C56,192 24,216 -4,246" fill="none" stroke="var(--navy)" stroke-width="5"/>
  </svg>

  <div class="person">
    <div class="person-name">Daniel Carter</div>
    <div class="person-title">President</div>
  </div>

  <div class="brand"><span class="brand-dot"></span>TIDE HARBOR</div>

  <ul class="contacts">
    <li><svg viewBox="0 0 24 24"><path d="M6.6 10.8a15.1 15.1 0 0 0 6.6 6.6l2.2-2.2c.3-.3.7-.4 1-.2 1.1.4 2.3.6 3.6.6.6 0 1 .4 1 1V20c0 .6-.4 1-1 1C10.6 21 3 13.4 3 4c0-.6.4-1 1-1h3.5c.6 0 1 .4 1 1 0 1.3.2 2.5.6 3.6.1.3 0 .7-.2 1z"/></svg>555-204-7713</li>
    <li><svg viewBox="0 0 24 24"><path d="M7 1h10a2 2 0 0 1 2 2v18a2 2 0 0 1-2 2H7a2 2 0 0 1-2-2V3a2 2 0 0 1 2-2zm0 3v15h10V4z"/></svg>555-318-4406</li>
    <li><svg viewBox="0 0 24 24"><path d="M2 5h20v14H2zm2 2v.5l8 5 8-5V7z"/></svg>name@tideharbor.com</li>
  </ul>

  <div class="address">
    4120 Willow Bend Road<br>
    Juneau, Alaska 99801<br>
    www.tideharbor.com
  </div>
</section>

</body>
</html>
```